Valtera Drones webdesign: Innovative Drones service company in agriculture

We need a new website according the following conditions:
• Main colour orange and current logo;
• Transparent – open – trustworthy – dynamic - personal;
• Use the smartness and overview characteristics of the crow (Valtera is Latin for crow);
• Accessible to multiple target groups and markets:
o So not too horticultural, too green;
• Use contradictions:
o Future versus nostalgia;
o Smartness crow versus precision hummingbird;
o Technology versus mechanical;
• Kestam 2.4 GTR as a style icon?
• Long pager website
Updates

Website menu o Home o Crop monitoring  Applications Growth | Stress | Development | Diseases  Markets Breeding | Young plant | Potplants | Cutflowers | Vegetables | Soft fruit  Customer cases o Technology Aerial data collection | Artificial intelligence | Free data sets o About Vision | Company | Partners | Team | Career o Contact o News&downloads Logo: www.valteradrones-example.com

Target Market(s)

agriculture: owners, crop managers
oil&gas: maintenance, quality control managers and purchase managers
logistics: ware house managers, purchase managers

Industry/Entity Type

Agribusiness

Number of Pages Required

2 page

Colors
f78f20

Requirements
Must have
• long pager website
downloads
social link
Should not have
• Not too 'green' because first impression of designers of agriculture/horticulture is using the green colour. But that is not necessary.

Keep in mind that the current logo will be updates: the circle will be more 'general' and less 'agri'. Also the green colors in the logo will be slightly darker to make it more powerful.

```html
<!DOCTYPE html>
<html lang="en">
<head>
<meta charset="utf-8">
<title>Valtera Drones – Crop Monitoring</title>
<link href="https://fonts.googleapis.com/css2?family=Lato:wght@300;400;700&display=swap" rel="stylesheet">
<style>
:root{
  --orange:#f7823a;
  --text:#555;
  --muted:#6a6a6a;
  --field:#d6d6d6;
  --footer:#666;
  --white:#fff;
  --rule:#777;
}
*{box-sizing:border-box;margin:0;padding:0}
html,body{width:1200px;height:2812px;overflow:hidden;background:var(--white)}
body{position:relative;font-family:'Lato',sans-serif;color:var(--text)}
.abs{position:absolute}
.brand{left:64px;top:36px;display:flex;align-items:center;gap:8px;color:var(--orange);font-size:20px;font-weight:400;letter-spacing:.5px;white-space:nowrap}
.brand-dot{width:36px;height:36px;border-radius:50%;background:var(--orange);flex:none}
.nav{top:47px;font-size:12px;font-weight:700;color:#555;letter-spacing:.2px;white-space:nowrap}
.hero{left:63px;top:128px;width:1067px;height:255px;
  background:linear-gradient(100deg,#4f6b3c 0%,#3d6b2a 35%,#7a8f52 55%,#b8584a 70%,#c9c3bb 85%,#5c7a3a 100%)}
.hero-title{left:131px;top:186px;width:310px;color:var(--white);font-size:36px;font-weight:300;line-height:45px}
.h2{color:var(--orange);font-size:37px;font-weight:300;line-height:44px;white-space:nowrap}
.copy{font-size:19px;font-weight:300;line-height:22.6px;color:var(--text)}
.copy p+p{margin-top:22.6px}
.intro{left:134px;top:470px;width:920px}
.icon{width:234px;height:234px;border-radius:50%;border:9px solid var(--orange);background:#fde6d6}
.body{left:437px;width:615px}
.rule{left:63px;top:2104px;width:1066px;height:1px;background:var(--rule)}
.form-title{left:132px;top:2140px;font-size:39px;font-weight:300;color:var(--orange);letter-spacing:2px;white-space:nowrap}
.form-copy{left:135px;top:2210px;width:335px;font-size:18px;font-weight:300;line-height:22.4px;letter-spacing:.8px;color:var(--muted)}
.form-copy p+p{margin-top:22.4px}
.label{right:606px;font-size:17.5px;font-weight:300;color:var(--muted);text-align:right;white-space:nowrap}
.field{left:638px;width:309px;height:20px;background:var(--field)}
.send{left:640px;top:2389px;width:134px;height:35px;border:2px solid #444;border-radius:18px;font-size:12px;color:#444;display:flex;align-items:center;justify-content:center;letter-spacing:.5px}
.footer{left:62px;top:2516px;width:1069px;height:296px;background:var(--footer);color:var(--white)}
.f-col{position:absolute;font-size:14.5px;line-height:18px;letter-spacing:.8px;white-space:nowrap}
.f-head{font-size:18px;font-weight:700;letter-spacing:1.2px;line-height:22px}
.social{position:absolute;left:86px;top:157px;width:40px;height:40px;border-radius:50%;background:var(--white)}
</style>
</head>
<body>

<header>
  <div class="abs brand"><span class="brand-dot"></span><span>Valtera Drones</span></div>
  <nav>
    <span class="abs nav" style="left:281px">HOME</span>
    <span class="abs nav" style="left:349px">CROP MONITORING</span>
    <span class="abs nav" style="left:506px">MARKETS</span>
    <span class="abs nav" style="left:596px">CUSTOMER CASES</span>
    <span class="abs nav" style="left:730px">TECHNOLOGY</span>
    <span class="abs nav" style="left:843px">ABOUT</span>
    <span class="abs nav" style="left:910px">CONTACTS</span>
    <span class="abs nav" style="left:1001px">NEW &amp; DOWNLOADS</span>
  </nav>
</header>

<section>
  <div class="abs hero" role="img" aria-label="Photo of a drone flying over rows of flowering plants in a greenhouse"></div>
  <h1 class="abs hero-title">Lorem ipsum dolor sit amet, consect etur adipiscing elit.</h1>
</section>

<section>
  <h2 class="abs h2" style="left:134px;top:410px">Crop Monitoring</h2>
  <div class="abs copy intro">Fusce placerat risus sit amet lectus egestas, pretium porttitor nisi facilisis. Morbi pellentesque odio et nulla interdum viverra. Nam suscipit, eros ut vulputate ultrices, libero odio mollis justo, nec varius felis odio ut mi. Sed felis nisl, congue at finibus in, porttitor ut elit. Etiam et mattis ipsum. Praesent vel molestie mi. Duis in nunc nunc. Class aptent taciti sociosqu ad litora torquent per conubia nostra, per inceptos himenaeos. Cras eget leo urna.</div>

  <h2 class="abs h2" style="left:133px;top:640px">Plant Growth</h2>
  <div class="abs icon" style="left:134px;top:706px" role="img" aria-label="Icon of a hand holding a sprouting plant"></div>
  <div class="abs copy body" style="top:703px">Pellentesque sit amet tristique elit. Aliquam semper ultricies nulla nec molestie. Nulla facilisi. Cum sociis natoque penatibus et magnis dis parturient montes, nascetur ridiculus mus. Morbi ut eros vitae purus hendrerit efficitur eget et nulla. Ut tincidunt sit amet mauris eu tempor. Curabitur ornare vitae sem nec tempus. Morbi laoreet metus neque, eu hendrerit magna interdum a. Aliquam erat volutpat. Nam auctor ut augue eu varius. Cras elementum accumsan pellentesque. Mauris nec nisi id ante faucibus consectetur. Aenean ornare aliquet neque, a fermentum odio vulputate sed. Morbi congue purus finibus ex cursus, euismod sagittis leo ornare.</div>

  <h2 class="abs h2" style="left:133px;top:980px">Stress</h2>
  <div class="abs icon" style="left:135px;top:1046px" role="img" aria-label="Icon of a ladybug"></div>
  <div class="abs copy body" style="top:1043px">
    <p>Integer maximus, leo ac ornare scelerisque, arcu mauris vulputate ex, id condimentum dolor augue sit amet nunc. Vestibulum maximus dapibus luctus. Etiam et dui ante. Phasellus malesuada nunc sit amet dui consequat, in faucibus sapien laoreet. Duis ac arcu quis elit ullamcorper rutrum vitae id dolor. Nunc feugiat nunc sit amet efficitur egestas. Morbi nec velit lorem.</p>
    <p>Duis eget nunc luctus, mattis quam vitae, posuere ipsum. Suspendisse interdum pretium velit, nec venenatis leo fringilla in. Pellentesque ut molestie velit. Etiam maximus, velit vel mattis congue, sapien libero convallis lacus, at sollicitudin magna ligula vitae quam. Maecenas id ante ac ex tincidunt sodales.</p>
  </div>

  <h2 class="abs h2" style="left:133px;top:1331px">Plant Development</h2>
  <div class="abs icon" style="left:135px;top:1397px" role="img" aria-label="Icon of a young plant with leaves growing from soil"></div>
  <div class="abs copy body" style="top:1394px">
    <p>Lorem ipsum dolor sit amet, consectetur adipiscing elit. Morbi ultricies molestie orci. Aenean purus mauris, sodales nec diam dignissim, porttitor laoreet enim. Aliquam id sollicitudin turpis. Vivamus aliquet elit sem, et ornare ex aliquam in. In cursus, felis non pretium molestie, tellus lacus facilisis metus, ut accumsan nisi nulla accumsan risus. Etiam id pharetra ante. Nunc sit amet ante id justo consequat tempor. Nullam pretium arcu eu hendrerit aliquam. Sed in purus eros.</p>
    <p>Fusce placerat risus sit amet lectus egestas, pretium porttitor nisi facilisis. Morbi pellentesque odio et nulla interdum viverra. Nam suscipit, eros ut vulputate ultrices, libero odio mollis justo, nec varius felis odio ut mi. Sed felis nisl, congue at finibus in, porttitor ut elit. Etiam et mattis ipsum. Praesent vel molestie mi. Duis in nunc nunc. Class aptent taciti sociosqu ad litora torquent per conubia nostra, per inceptos himenaeos. Cras eget leo urna.</p>
  </div>

  <h2 class="abs h2" style="left:133px;top:1750px">Disreases Market</h2>
  <div class="abs icon" style="left:134px;top:1816px" role="img" aria-label="Icon of a magnifying glass over a leaf"></div>
  <div class="abs copy body" style="top:1813px">
    <p>Quisque egestas feugiat turpis, vel sagittis dui finibus molestie. Morbi non ante id dui rhoncus consectetur. Maecenas malesuada libero lorem, quis feugiat mauris semper non. Maecenas a lobortis nisl. Praesent vitae vulputate lorem. Quisque pretium tristique euismod. Proin eget vehicula sapien.</p>
    <p>Integer maximus, leo ac ornare scelerisque, arcu mauris vulputate ex, id condimentum dolor augue sit amet nunc. Vestibulum maximus dapibus luctus. Etiam et dui ante. Phasellus malesuada nunc sit amet dui consequat, in faucibus sapien laoreet. Duis ac arcu quis elit ullamcorper rutrum vitae id dolor. Nunc feugiat nunc sit amet efficitur egestas. Morbi nec velit lorem. Duis eget nunc luctus, mattis quam vitae, posuere ipsum. Suspendisse</p>
  </div>
</section>

<div class="abs rule"></div>

<section>
  <h2 class="abs form-title">What’s on your mind?</h2>
  <div class="abs form-copy">
    <p>Curabitur ornare vitae sem nec tempus. Morbi laoreet metus neque, eu hendrerit magna interdum a. Aliquam erat volutpat. Nam auctor ut augue eu varius.</p>
    <p>Cras elementum accumsan pellentesque. Mauris nec nisi id ante faucibus consectetur. Aenean ornare aliquet neque, a fermentum odio vulputate sed.</p>
  </div>
  <span class="abs label" style="top:2214px">Email</span>
  <span class="abs label" style="top:2244px">First Name</span>
  <span class="abs label" style="top:2274px">Last Name</span>
  <span class="abs label" style="top:2304px">Message</span>
  <div class="abs field" style="top:2218px"></div>
  <div class="abs field" style="top:2248px"></div>
  <div class="abs field" style="top:2278px"></div>
  <div class="abs field" style="top:2302px;height:60px"></div>
  <div class="abs send">SEND</div>
</section>

<footer class="abs footer">
  <div class="f-col" style="left:78px;top:25px">
    <div class="f-head">WHY DON’T YOU DROP BY?</div>
    <div style="margin-top:23px">Lindenhoflaan 14B,<br>4821KT, Marwijk<br>Email: info@valteradrones-example.com<br>Telephone: +31 6 55501234</div>
  </div>
  <div class="social" role="img" aria-label="Social profile link"></div>
  <div class="f-col" style="left:418px;top:24px">
    <div class="f-head">CROP MONITORING</div>Growth<br>Stress<br>Development<br>Diseases
  </div>
  <div class="f-col" style="left:418px;top:149px">
    <div class="f-head">MARKETS</div>Breeding<br>Young plant<br>Potplants<br>Cutflowers<br>Vegetables<br>Soft fruit
  </div>
  <div class="f-col" style="left:628px;top:24px">
    <div class="f-head">TECHNOLOGY</div>Aerial data collection<br>Artificial intelligence<br>Free data sets
  </div>
  <div class="f-col" style="left:628px;top:149px"><div class="f-head">NEWS &amp; DOWNLOADS</div></div>
  <div class="f-col" style="left:628px;top:200px"><div class="f-head">CUSTOMER CASES</div></div>
  <div class="f-col" style="left:869px;top:24px">
    <div class="f-head">ABOUT</div>Vision<br>Company<br>Partners<br>Team<br>Career
  </div>
  <div class="f-col" style="left:869px;top:149px"><div class="f-head">FREE DATA SETS</div></div>
  <div class="f-col" style="left:869px;top:200px"><div class="f-head">CONTACT</div></div>
</footer>

</body>
</html>
```